BrightOak Lending Needs a Stated Income Flyer

We need a flyer created for our Stated Income loan program, using the color scheme to match our company logo.
I've included a stock photo to be used and within that photo, we want Funded stamped in red on the blank poster board.
For the written part of the flyer, we want the word State Income in red.
On the bottom part (Contact Us), we want to make it possible for us to edit for any future loan officer we hire along the way to include their contact information.
We like the flyer for VeroCredit.
Industry/Entity Type
Loan

```html
<!DOCTYPE html>
<html lang="en">
<head>
<meta charset="utf-8">
<title>BrightOak Lending – Stated Income</title>
<link href="https://fonts.googleapis.com/css2?family=Oswald:wght@600;700&family=Arimo:ital,wght@0,400;0,700;1,400;1,700&display=swap" rel="stylesheet">
<style>
:root{
  --red:#e2231a;
  --navy:#1b3767;
  --blue:#2b5fa8;
  --sky:#d3e6f5;
  --sky-deep:#a9cbe8;
  --ink:#333;
  --white:#fff;
}
html,body{margin:0;padding:0;overflow:hidden;background:var(--white);}
.flyer{position:relative;width:851px;height:1200px;overflow:hidden;background:var(--white);font-family:"Arimo",Arial,sans-serif;}
.headline{position:absolute;top:18px;left:0;width:100%;text-align:center;margin:0;font-family:"Oswald",Impact,sans-serif;font-weight:700;font-size:104px;line-height:1;color:var(--red);letter-spacing:1px;}
.tagline{position:absolute;top:128px;left:0;width:100%;text-align:center;margin:0;font-style:italic;font-weight:700;font-size:33px;color:var(--navy);}
.product-band{position:absolute;top:205px;left:0;width:100%;height:80px;background:linear-gradient(180deg,#3a72bd,var(--blue) 60%,#214d8f);text-align:center;color:var(--white);}
.product-band h2{margin:8px 0 0;font-style:italic;font-weight:700;font-size:36px;letter-spacing:.5px;}
.product-band p{margin:4px 0 0;font-style:italic;font-weight:700;font-size:22px;}
.photo{position:absolute;top:285px;left:0;width:470px;height:385px;background:radial-gradient(ellipse at 45% 45%,#efe6dc 0%,#d9c2ad 45%,#9fb0c6 100%);}
.benefits{position:absolute;top:396px;left:486px;width:352px;margin:0;padding:0;list-style:none;}
.benefits li{font-style:italic;font-size:20px;color:var(--navy);line-height:1.1;margin-bottom:8px;}
.benefits b{color:var(--red);font-weight:700;margin-right:6px;}
.badge{position:absolute;top:455px;left:358px;width:124px;height:116px;}
.badge svg{display:block;width:124px;height:116px;}
.badge span{position:absolute;left:0;width:100%;text-align:center;color:var(--white);font-style:italic;font-weight:700;font-size:19px;line-height:1.05;top:30px;}
.rates-band{position:absolute;top:655px;left:0;width:100%;height:130px;}
.rates{position:absolute;top:668px;left:0;width:100%;text-align:center;margin:0;font-family:"Oswald",Impact,sans-serif;font-weight:600;font-size:44px;color:var(--navy);}
.terms{position:absolute;top:728px;left:0;width:100%;text-align:center;margin:0;font-style:italic;font-weight:700;font-size:25px;color:var(--navy);}
.facts{position:absolute;top:775px;left:0;width:100%;height:200px;background:var(--navy);}
.facts ul{list-style:none;margin:0;padding:18px 0 0;text-align:center;color:var(--white);}
.facts li{font-style:italic;font-weight:700;font-size:30px;line-height:42px;}
.footer-curve{position:absolute;top:960px;left:0;width:851px;height:60px;}
.brand{position:absolute;top:1030px;left:40px;display:flex;align-items:center;gap:10px;font-weight:700;font-size:30px;color:var(--navy);}
.brand i{display:block;width:26px;height:26px;background:var(--blue);}
.contact{position:absolute;top:1010px;right:30px;text-align:right;color:var(--navy);font-size:17px;line-height:27px;font-style:normal;}
.contact .name{font-weight:700;font-size:21px;}
.contact .row{display:flex;justify-content:flex-end;align-items:center;gap:10px;}
.contact svg{width:14px;height:14px;fill:var(--red);}
.disclaimer{position:absolute;top:1140px;left:20px;right:20px;border-top:1px solid #bbb;padding-top:8px;margin:0;font-size:10.5px;line-height:1.35;color:var(--ink);text-align:center;}
</style>
</head>
<body>
<main class="flyer">
  <h1 class="headline">STATED INCOME</h1>
  <p class="tagline">Qualifying Real Estate Investors Just Got Easier!</p>

  <section class="product-band">
    <h2>PURCHASE &amp; CASH OUT REFINANCE</h2>
    <p>Non-owner SFR/Condo/2-4 Units - 5+ Units &amp; Commercial – Ask for Details</p>
  </section>

  <div class="photo" role="img" aria-label="Smiling group of business people holding a poster board stamped FUNDED in red"></div>

  <ul class="benefits">
    <li><b>NO</b>Tax Returns</li>
    <li><b>NO</b>4506-T</li>
    <li><b>NO</b>Cash-Out Restrictions</li>
    <li><b>NO</b>Cash Reserves Required</li>
    <li><b>NO</b>Limit on Number of Properties owned or financed</li>
    <li><b>NO</b>DTI Calculation</li>
    <li><b>NO</b>Seasoned Funds – No Asset Disclosures (Purchase)</li>
  </ul>

  <div class="badge">
    <svg viewBox="0 0 160 150">
      <polygon fill="#e2231a" points="80,2 95,25 122,12 120,42 152,45 133,70 156,92 126,100 134,130 106,120 96,148 80,126 64,148 54,120 26,130 34,100 4,92 27,70 8,45 40,42 38,12 65,25"/>
    </svg>
    <span>FAST<br>&amp;<br>EASY</span>
  </div>

  <svg class="rates-band" viewBox="0 0 851 130" preserveAspectRatio="none">
    <path d="M0,20 Q425,-10 851,20 L851,130 L0,130 Z" fill="var(--sky)"/>
    <path d="M0,110 Q425,95 851,110 L851,130 L0,130 Z" fill="var(--sky-deep)"/>
  </svg>
  <p class="rates">RATES - 7.49% (BUYS DOWNS TO 6.49%)</p>
  <p class="terms">3 &amp; 5 Year Fixed ARM – 30 Year Amortization</p>

  <section class="facts">
    <ul>
      <li>Max 70% Loan-to-value</li>
      <li>650 Min Credit Score</li>
      <li>Loan Amounts $100,000 to $2,000,000</li>
      <li>Lending to Corporations, LLC, Partnership &amp; Individuals</li>
    </ul>
  </section>
  <svg class="footer-curve" viewBox="0 0 851 60" preserveAspectRatio="none">
    <path d="M0,0 L851,0 L851,15 Q425,70 0,15 Z" fill="var(--navy)"/>
  </svg>

  <div class="brand"><i></i>BrightOak Lending</div>

  <address class="contact">
    <div class="row name">MARCUS DELANE <svg viewBox="0 0 14 14"><circle cx="7" cy="4" r="3"/><path d="M1,14 Q7,5 13,14Z"/></svg></div>
    <div class="row">555-014-2290 <svg viewBox="0 0 14 14"><path d="M3,1 L6,4 L4.5,6 Q6,9 8,9.5 L10,8 L13,11 L11,13 Q3,12 1,3 Z"/></svg></div>
    <div class="row">marcus@brightoaklending.com <svg viewBox="0 0 14 14"><path d="M1,3 H13 V11 H1 Z M1,3 L7,8 L13,3" stroke="#fff" stroke-width="1"/></svg></div>
    <div class="row">BRE #00000000 <svg viewBox="0 0 14 14"><rect x="2" y="2" width="10" height="10"/></svg></div>
  </address>

  <p class="disclaimer">Intended for mortgage professional only and not intended for consumer use as defined by Section 226.2 of Regulation Z. Financing subject to credit evaluation, approval of collateral and other requirements. Non regulation Z covered loans. Terms and conditions subject to change without notice. BrightOak Lending is licensed by the California Bureau of Real Estate, BRE License No. 00000000 NMLS ID 000000. 1200 Harbor View Lane, Suite 100, Irvine, CA 92000.</p>
</main>
</body>
</html>
```